Revamp Of Landing Page For an Automated AI Voice Agents Agency

here is my current landing page https://app.brightfunnelstudio.example/v2/preview/KXWQPmR4hLsDnTfYvJcA?notrack=true

Please use all my current content and imagery of ai agents in your new design. Make it easy to ready, easy to navigate and easy to understand

I am looking for a SLEEK shiny polished looking website. I like Dark themed sites but am open to see light themed sites too so please dont be shy.

The site should have an Ai Voice Agent Theme about it. Maybe look and feel of futureistic but simple and not intimidating to the average person...

Here are a couple website designs I like for reference:
https://q4t.example/
https://ai-bots.mervinholt.example/
https://chatvexo.example/ai-agents

Target Market(s)

b2b

Industry/Entity Type

AI Voice Agents

Coding

Coded - Design and coding required

Font styles to use
Other font styles liked:
• open

Requirements
Must have
• all elements and content and images used in existing design.
Nice to have
• open
Should not have
• open

```html
<!DOCTYPE html>
<html lang="en">
<head>
<meta charset="utf-8">
<title>Voxline Agents — Intelligent Voice Agents</title>
<link rel="stylesheet" href="https://fonts.googleapis.com/css2?family=Lexend:wght@400;500;600&family=Inter:wght@400;500;600&display=swap">
<style>
:root{
  --bg:#0e0622;
  --bg-deep:#0a041a;
  --panel:#1a0c3a;
  --violet:#6c3ff0;
  --violet-2:#8a4df5;
  --violet-soft:#7b5cff;
  --line:rgba(160,120,255,.35);
  --text:#ffffff;
  --muted:#d6d0e8;
  --accent-text:#8f7bff;
  --star:#ffd400;
}
*{box-sizing:border-box;margin:0;padding:0}
html,body{width:1200px;height:3795px;overflow:hidden}
body{background:var(--bg);color:var(--text);font-family:"Inter",Arial,sans-serif;position:relative}
.abs{position:absolute}
h1,h2,h3,.display{font-family:"Lexend",Arial,sans-serif;font-weight:500;text-transform:uppercase;letter-spacing:.5px}
.btn{position:absolute;display:flex;align-items:center;justify-content:center;border-radius:999px;font-size:12px;font-weight:500;color:#fff}
.btn-fill{background:linear-gradient(90deg,var(--violet),var(--violet-2))}
.btn-line{border:1.5px solid rgba(255,255,255,.55)}
.brand{font-family:"Lexend",Arial,sans-serif;font-weight:500;font-size:22px;letter-spacing:1px;display:flex;align-items:center;gap:8px}
.brand .dot{width:14px;height:14px;border-radius:50%;background:var(--violet-soft)}
.eyebrow{color:var(--accent-text);font-size:14px;display:flex;align-items:center;gap:8px}
.eyebrow::before,.eyebrow::after{content:"";width:46px;height:1px;background:var(--accent-text)}
.eyebrow.left::before{display:none}
.section-title{position:absolute;left:0;width:1200px;text-align:center;font-size:25px}

/* hero */
.hero{position:absolute;left:0;top:0;width:1200px;height:706px;background:radial-gradient(ellipse at 50% 45%,#4a1d8c 0%,#2a0f5c 40%,#12072a 80%)}
.hero-art{position:absolute;left:0;top:190px;width:1200px;height:516px;background:radial-gradient(circle at 660px 195px,rgba(120,70,230,.55) 0,rgba(60,20,120,.25) 180px,transparent 420px),linear-gradient(100deg,rgba(210,210,225,.25) 0%,transparent 35%,transparent 70%,rgba(230,170,140,.22) 100%)}
.hero h1{position:absolute;top:88px;left:0;width:1200px;text-align:center;font-size:34px;line-height:44px}
.topline{position:absolute;left:122px;top:68px;width:955px;height:1px;background:rgba(255,255,255,.12)}

/* agent cards */
.agent-card{position:absolute;top:786px;width:468px;height:318px;border:1px solid var(--line);border-radius:8px;overflow:hidden;background:linear-gradient(180deg,#5a6b7e 0%,#2b2f4a 55%,#1a0d3c 100%)}
.agent-card .shade{position:absolute;inset:0;background:linear-gradient(180deg,transparent 45%,rgba(25,10,60,.92) 75%)}
.agent-card h3{position:absolute;left:20px;top:210px;font-size:18px}
.agent-card p{position:absolute;left:18px;top:245px;width:390px;font-size:10.5px;line-height:18px;color:var(--muted)}
.arrow-dot{position:absolute;width:36px;height:36px;border-radius:50%;background:var(--violet-2);display:flex;align-items:center;justify-content:center}
.agent-card .arrow-dot{right:24px;bottom:24px}
.slider-arrow{position:absolute;top:930px;width:32px;height:32px;border:1.5px solid var(--violet-soft);border-radius:50%;display:flex;align-items:center;justify-content:center}

/* features */
.feature{position:absolute;top:1223px;width:306px;height:190px;border:1px solid var(--line);border-radius:8px;background:linear-gradient(135deg,#23104a 0%,#170a33 60%,#3a1a72 100%)}
.feature .icon{position:absolute;left:24px;top:26px;width:58px;height:58px;border-radius:50%;border:1.5px solid #fff;display:flex;align-items:center;justify-content:center}
.feature h3{position:absolute;left:24px;top:116px;font-family:"Inter",Arial,sans-serif;text-transform:none;font-size:17px;font-weight:500;letter-spacing:0}
.feature p{position:absolute;left:24px;top:146px;font-size:9.5px;color:var(--muted)}
.feature .arrow-dot{right:14px;bottom:14px;width:30px;height:30px}

/* about */
.about{position:absolute;left:0;top:1476px;width:1200px;height:486px;background:linear-gradient(160deg,#170936 0%,#12072a 55%,#3c1a6e 100%);border-top:1px solid rgba(255,255,255,.06)}
.about-photo{position:absolute;left:122px;top:33px;width:486px;height:415px;border-radius:8px;background:linear-gradient(120deg,#cfd7de 0%,#8aa0b3 40%,#4f6a80 100%)}
.about-copy{position:absolute;left:690px;top:84px;width:360px}
.about-copy h2{font-size:24px;line-height:30px;margin-top:14px}
.about-copy .lead{font-size:9.5px;font-weight:600;margin-top:10px}
.about-copy p{font-size:10.5px;line-height:19px;color:var(--muted);margin-top:4px}
.perks{display:flex;gap:48px;margin-top:16px}
.perk .ic{width:34px;height:34px;border:1.5px solid #fff;border-radius:50%;display:flex;align-items:center;justify-content:center}
.perk span{display:block;font-size:15px;line-height:20px;margin-top:8px}

/* faq */
.dots{position:absolute;left:0;top:1966px;width:1200px;height:320px;background-image:radial-gradient(rgba(120,90,220,.25) 1.2px,transparent 1.4px);background-size:12px 12px;-webkit-mask-image:linear-gradient(180deg,#000,transparent);mask-image:linear-gradient(180deg,#000,transparent)}
.faq-item{position:absolute;left:234px;width:730px;height:117px;border:1px solid rgba(160,120,255,.3);border-radius:10px;background:rgba(20,8,45,.6)}
.faq-item .num{position:absolute;left:30px;top:37px;width:44px;height:44px;border-radius:50%;background:var(--violet-2);display:flex;align-items:center;justify-content:center;font-size:17px;font-weight:600}
.faq-item h3{position:absolute;left:113px;top:22px;font-family:"Inter",Arial,sans-serif;text-transform:none;letter-spacing:0;font-size:17px;font-weight:500}
.faq-item p{position:absolute;left:113px;top:58px;width:450px;font-size:10.5px;line-height:19px;color:var(--muted)}
.faq-item .toggle{position:absolute;right:26px;top:58px;width:14px;height:1.5px;background:#fff}

/* testimonial */
.review{position:absolute;left:122px;top:2651px;width:955px;height:374px;border:1px solid var(--line);border-radius:10px;background:linear-gradient(135deg,#2a1258 0%,#170a33 60%,#1e0d42 100%)}
.review .copy{position:absolute;left:40px;top:80px;width:382px;text-align:center}
.review .name{font-size:19px}
.stars{display:flex;justify-content:center;gap:4px;margin:8px 0 10px}
.review .quote{font-size:11.5px;line-height:22.5px;color:var(--muted)}
.video{position:absolute;left:442px;top:19px;width:494px;height:334px;border-radius:8px;background:linear-gradient(180deg,#bcc8d4 0%,#97a9b9 100%)}
.play{position:absolute;left:200px;top:120px;width:86px;height:86px;border-radius:50%;background:rgba(20,20,30,.75);border:2px solid rgba(255,255,255,.6);display:flex;align-items:center;justify-content:center}

/* cta */
.cta{position:absolute;left:0;top:3087px;width:1200px;height:281px;background:linear-gradient(160deg,#3a1670 0%,#1c0b3e 45%,#2a1256 75%,#5b2a9a 100%)}
.cta .eyebrow{position:absolute;top:54px;left:0;width:1200px;justify-content:center}
.cta h2{position:absolute;top:98px;left:0;width:1200px;text-align:center;font-size:29px;line-height:38px}

/* footer */
.footer{position:absolute;left:0;top:3368px;width:1200px;height:427px;background:var(--bg-deep);overflow:hidden}
.footer .divider{position:absolute;top:40px;width:1px;height:230px;background:rgba(255,255,255,.15)}
.footer h4{position:absolute;font-family:"Lexend",Arial,sans-serif;font-weight:500;font-size:14px;text-transform:uppercase}
.footer small{font-size:10.5px;line-height:19px;color:var(--muted)}
.contact-row{position:absolute;left:503px;display:flex;gap:10px;align-items:flex-start;font-size:10.5px;line-height:16px;color:var(--muted)}
.contact-row .ic{width:18px;height:18px;border:1px solid #fff;border-radius:50%;flex:none;display:flex;align-items:center;justify-content:center}
.email{color:var(--accent-text)}
.input{position:absolute;left:852px;top:135px;width:225px;height:37px;border:1px solid #fff;border-radius:999px;font-size:8.5px;padding-left:18px;display:flex;align-items:center}
.watermark{position:absolute;left:0;bottom:-22px;width:1200px;text-align:center;font-family:"Lexend",Arial,sans-serif;font-weight:500;font-size:128px;letter-spacing:6px;color:rgba(255,255,255,.05);white-space:nowrap}
</style>
</head>
<body>

<section class="hero">
  <div class="hero-art" role="img" aria-label="Robot hand and human hand reaching toward a glowing AI emblem over purple sound waves"></div>
  <div class="topline"></div>
  <div class="brand abs" style="left:122px;top:20px"><span>VOXLINE AGENTS</span><span class="dot"></span></div>
  <a class="btn btn-fill" style="left:861px;top:25px;width:102px;height:30px">Login</a>
  <a class="btn btn-line" style="left:977px;top:25px;width:100px;height:30px">Sign up</a>
  <h1>Empower conversations with<br>intelligent voice agents</h1>
  <a class="btn btn-fill" style="left:436px;top:540px;width:157px;height:49px">Get Started</a>
  <a class="btn btn-line" style="left:606px;top:540px;width:158px;height:49px">Free demo</a>
</section>

<div class="eyebrow abs" style="left:0;top:694px;width:1200px;justify-content:center">Tecnology</div>
<h2 class="section-title" style="top:725px">Meet your new AI-powered workforce</h2>

<a class="slider-arrow" style="left:61px"><svg width="10" height="10" viewBox="0 0 10 10"><path d="M6.5 1 2.5 5l4 4" stroke="#8f7bff" stroke-width="1.5" fill="none"/></svg></a>
<a class="slider-arrow" style="left:1110px"><svg width="10" height="10" viewBox="0 0 10 10"><path d="M3.5 1 7.5 5l-4 4" stroke="#8f7bff" stroke-width="1.5" fill="none"/></svg></a>

<article class="agent-card" style="left:122px">
  <div class="abs" role="img" aria-label="AI sales agent wearing a headset in a city office" style="inset:0"></div>
  <div class="shade"></div>
  <h3>AI Sales</h3>
  <p>Brian will take your inbound sales calls. Will give all detailed information to the customer, answer questions in a normal conversational tone and can book sales appointments or transfer hot prospects to a human to close the sale.</p>
  <span class="arrow-dot"><svg width="12" height="12" viewBox="0 0 12 12"><path d="M3 9 9 3M4 3h5v5" stroke="#fff" stroke-width="1.5" fill="none"/></svg></span>
</article>
<article class="agent-card" style="left:609px;background:linear-gradient(180deg,#2f8aa6 0%,#24506e 55%,#1a0d3c 100%)">
  <div class="abs" role="img" aria-label="AI lead qualifier agent wearing a headset at a desk" style="inset:0"></div>
  <div class="shade"></div>
  <h3>AI Lead Qualifier</h3>
  <p>All of our ai agents gather information and qualify leads. If they are interestedin the services on the call then our ai agents will assist them with booking anappointment with our sales team over the call.</p>
  <span class="arrow-dot"><svg width="12" height="12" viewBox="0 0 12 12"><path d="M3 9 9 3M4 3h5v5" stroke="#fff" stroke-width="1.5" fill="none"/></svg></span>
</article>

<h2 class="section-title" style="top:1162px">An employee that never gets sick!</h2>

<div class="feature" style="left:122px">
  <span class="icon"><svg width="24" height="24" viewBox="0 0 24 24" fill="none" stroke="#fff" stroke-width="1.6"><path d="M9 3a4 4 0 0 0-4 4 3.5 3.5 0 0 0 0 7 4 4 0 0 0 4 4V3zM15 3a4 4 0 0 1 4 4 3.5 3.5 0 0 1 0 7 4 4 0 0 1-4 4V3z"/></svg></span>
  <h3>Trained In Seconds</h3><p>Learns Your Entire Website In Seconds</p>
  <span class="arrow-dot"><svg width="11" height="11" viewBox="0 0 12 12"><path d="M3 9 9 3M4 3h5v5" stroke="#fff" stroke-width="1.5" fill="none"/></svg></span>
</div>
<div class="feature" style="left:446px">
  <span class="icon"><svg width="24" height="24" viewBox="0 0 24 24" fill="none" stroke="#fff" stroke-width="1.6"><circle cx="12" cy="12" r="9"/><path d="M3 12h18M12 3c3 3 3 15 0 18M12 3c-3 3-3 15 0 18"/></svg></span>
  <h3>Worldwide</h3><p>Works Anywhere In The Globe</p>
  <span class="arrow-dot"><svg width="11" height="11" viewBox="0 0 12 12"><path d="M3 9 9 3M4 3h5v5" stroke="#fff" stroke-width="1.5" fill="none"/></svg></span>
</div>
<div class="feature" style="left:771px">
  <span class="icon"><svg width="24" height="24" viewBox="0 0 24 24" fill="#fff"><circle cx="9" cy="9" r="3.2"/><circle cx="16" cy="9" r="2.6"/><path d="M3 19c0-3.5 3-5.5 6-5.5s6 2 6 5.5zM14 19c0-2-.6-3.4-1.6-4.4 3.6-.8 7.6.6 7.6 4.4z"/></svg></span>
  <h3>User-friendly</h3><p>Your Ai Agents Sound As If They're Real Humans</p>
  <span class="arrow-dot"><svg width="11" height="11" viewBox="0 0 12 12"><path d="M3 9 9 3M4 3h5v5" stroke="#fff" stroke-width="1.5" fill="none"/></svg></span>
</div>

<section class="about">
  <div class="about-photo" role="img" aria-label="Humanoid AI agents with headsets working at laptops in a bright office"></div>
  <div class="about-copy">
    <div class="eyebrow left">About Us</div>
    <h2>Install the power of<br>AI for your business</h2>
    <div class="lead">Your New Ai Agents Will Never Call In Sick And Will Never Complain!</div>
    <p>With your new team of AI Agents, handling inbound calls, sending emails &amp; sms messages, booking appointments &amp; handling customer serviceinquiries is going to save you a ton of time and money.</p>
    <div class="perks">
      <div class="perk"><span class="ic"><svg width="16" height="16" viewBox="0 0 16 16" fill="none" stroke="#fff" stroke-width="1.4"><circle cx="8" cy="7" r="4.5"/><path d="M8 4.5v5M6.5 6h2.5a1 1 0 0 1 0 2H7"/></svg></span><span>14-day money<br>-back guarantee</span></div>
      <div class="perk"><span class="ic"><svg width="16" height="16" viewBox="0 0 16 16" fill="none" stroke="#fff" stroke-width="1.4"><path d="M3 9V8a5 5 0 0 1 10 0v1"/><rect x="2" y="9" width="3" height="4" rx="1"/><rect x="11" y="9" width="3" height="4" rx="1"/></svg></span><span>24/7 Customer<br>Support</span></div>
    </div>
    <a class="btn btn-fill" style="position:relative;margin-top:14px;width:158px;height:48px">Learn More</a>
  </div>
</section>

<div class="dots"></div>
<h2 class="section-title" style="top:2018px">Do you have questions ?</h2>
<div class="faq-item" style="top:2080px"><span class="num">01</span><h3>What exactly are the AI Voice Agents ?</h3><p>AI Voice Agents are specialized human sounding bots, having smart and masterful conversationsand each is expertly trained in seconds for a specific business function.</p><span class="toggle"></span></div>
<div class="faq-item" style="top:2217px"><span class="num">02</span><h3>How will these AI Voice Agents benefit</h3><p>Ai Voice Agents Answer Calls, Book Appts, Send Emails, Text Messages, Follow Up Reminders &amp; More For You 24/7!</p><span class="toggle"></span></div>
<div class="faq-item" style="top:2352px"><span class="num">03</span><h3>Are they easy to use ?</h3><p>We provide a done for you service. We create your AI Voice Agent and<br>launch it within days!</p><span class="toggle"></span></div>

<h2 class="section-title" style="top:2590px">What our clients says</h2>
<div class="review">
  <div class="copy">
    <div class="name">- Jonas Verhey</div>
    <div class="stars">
      <svg width="14" height="14" viewBox="0 0 24 24"><path fill="#ffd400" d="M12 2l3 7 7 .6-5.4 4.7 1.7 7.2L12 17.8 5.7 21.5l1.7-7.2L2 9.6 9 9z"/></svg>
      <svg width="14" height="14" viewBox="0 0 24 24"><path fill="#ffd400" d="M12 2l3 7 7 .6-5.4 4.7 1.7 7.2L12 17.8 5.7 21.5l1.7-7.2L2 9.6 9 9z"/></svg>
      <svg width="14" height="14" viewBox="0 0 24 24"><path fill="#ffd400" d="M12 2l3 7 7 .6-5.4 4.7 1.7 7.2L12 17.8 5.7 21.5l1.7-7.2L2 9.6 9 9z"/></svg>
      <svg width="14" height="14" viewBox="0 0 24 24"><path fill="#ffd400" d="M12 2l3 7 7 .6-5.4 4.7 1.7 7.2L12 17.8 5.7 21.5l1.7-7.2L2 9.6 9 9z"/></svg>
      <svg width="14" height="14" viewBox="0 0 24 24"><path fill="#ffd400" d="M12 2l3 7 7 .6-5.4 4.7 1.7 7.2L12 17.8 5.7 21.5l1.7-7.2L2 9.6 9 9z"/></svg>
    </div>
    <p class="quote">“Lorem ipsum dolor sit amet, consectetur adipiscing elit. Proin consequat metus gravida tellus ornare, vel pharetra justo maximus. Maecenas eleifend mattis dolor vitae faucibu. Phasellus a magna fringilla, porttitor nulla sed, finibus nibh. Sed viverra tristique sapien, vel efficitur est dictum quis. Donec ultricies cursus nisi, sit amet placerat arcu ultricies et.”</p>
  </div>
  <div class="video" role="img" aria-label="Video testimonial of a smiling client in a suit giving a thumbs up">
    <span class="play"><svg width="22" height="24" viewBox="0 0 22 24"><path d="M3 2l17 10L3 22z" fill="#fff"/></svg></span>
  </div>
</div>

<section class="cta">
  <div class="eyebrow">What are you waiting for?</div>
  <h2>Start your new journey with<br>effective AI solutions</h2>
  <a class="btn btn-fill" style="left:521px;top:177px;width:158px;height:48px">Contact Us</a>
</section>

<footer class="footer">
  <div class="brand abs" style="left:122px;top:58px"><span>VOXLINE AGENTS</span><span class="dot"></span></div>
  <div class="abs" style="left:122px;top:102px;width:200px"><small>Cprivacy &nbsp;&nbsp;| &nbsp;&nbsp;terms &amp; conditions<br>earnings &amp; products disclaimer<br>© 2025 Voxline Agents.</small></div>
  <span class="divider" style="left:397px"></span>
  <span class="divider" style="left:764px"></span>

  <h4 style="left:503px;top:62px">Contact Us</h4>
  <div class="contact-row" style="top:104px"><span class="ic"><svg width="9" height="9" viewBox="0 0 10 10"><path d="M5 9S1.5 5.5 1.5 3.8a3.5 3.5 0 0 1 7 0C8.5 5.5 5 9 5 9z" fill="none" stroke="#fff"/></svg></span><span>Havenstraat 12 9000<br>GhentBelgium BE 0000.111.222</span></div>
  <div class="contact-row" style="top:152px"><span class="ic"><svg width="9" height="9" viewBox="0 0 10 10"><path d="M2 1.5l2 .3.6 2-1 .8a5 5 0 0 0 2 2l.8-1 2 .6.3 2C5 8.5 1.5 5 2 1.5z" fill="none" stroke="#fff" stroke-width=".9"/></svg></span><span>+32 400 12 34 56</span></div>
  <div class="contact-row" style="top:182px"><span class="ic"><svg width="9" height="9" viewBox="0 0 10 10"><path d="M1 5l8-4-3 8-1.5-3z" fill="none" stroke="#fff" stroke-width=".9"/></svg></span><span class="email">hello@voxline.example</span></div>

  <h4 style="left:852px;top:62px">Subscribe Newsletter</h4>
  <div class="abs" style="left:852px;top:100px"><small>Subscribe To Our Newsletter</small></div>
  <div class="input">Enter Your Email</div>
  <a class="btn btn-fill" style="left:852px;top:185px;width:158px;height:49px">Subscribe</a>

  <div class="watermark">VOXLINE AGENTS</div>
</footer>

</body>
</html>
```